Coffee Bag Design for Tidewell Coffee

We’re excited to invite you to help us bring Tidewell Coffee to life on grocery store shelves with a design that embodies our mission of spreading goodness and creating a lasting impact. Tidewell Coffee represents warmth, positivity, and the power of small actions to create ripples of goodness. Each cup not only offers a rich, gourmet coffee experience but also gives back to the community, with $2 from each bag supporting local food banks.

To reflect this vision, we’d love for the design to feature a dark (greyish) blue as the base color to convey depth and quality, complemented by a vibrant light blue that will catch the eye and add energy. Tan or gold accents could add an elegant touch and a feeling of warmth. We are aiming for a look that feels uplifting and engaging, with simplicity and elegance, yet stands out amid other brands on the shelf.

I am attaching the dimension of the bag.

Other information that needs to be listed:
Ingredients: 100% Arabica Coffee
Net Wt. 12 oz. (340 g)
Roasted and distributed by:
Name
Address
email

Text on the back of the bag:
Tidewell Coffee is crafted with a belief that kindness and positivity can spread, Small acts, lasting ripples in every cup. This gourmet blend delivers a rich taste experience while giving back, as $2 from each bag sold is donated to local food banks to help those in need. Enjoy the warmth and goodness in each cup, knowing you’re making a difference with every purchase.

Thank you!

```html
<!DOCTYPE html>
<html lang="en">
<head>
<meta charset="UTF-8">
<title>Tidewell Coffee – Colombia Bag Front</title>
<link href="https://fonts.googleapis.com/css2?family=Josefin+Sans:wght@300;400&family=Montserrat:wght@500;600;700&display=swap" rel="stylesheet">
<style>
  :root {
    --backdrop: #f1f1f1;
    --bag-navy: #393752;
    --bag-navy-deep: #2f2d47;
    --bag-sky: #a6cedb;
    --tagline-blue: #3f7f9c;
    --gold: #c99a63;
    --label-frame: #3c4658;
    --label-paper: #f2ecd9;
    --ink: #3a3a3a;
    --ink-soft: #6b675d;
    --hatch: #cfc8b6;
    --leaf: #d9d1bb;
  }
  * { margin: 0; padding: 0; box-sizing: border-box; }
  html, body { width: 1200px; height: 900px; overflow: hidden; background: var(--backdrop); }
  .canvas { position: relative; width: 1200px; height: 900px; }

  .bag {
    position: absolute; left: 420px; top: 120px;
    width: 360px; height: 660px;
    background: linear-gradient(to bottom, var(--bag-navy) 0 422px, var(--bag-sky) 422px 100%);
    border-radius: 10px 10px 0 0;
    overflow: hidden;
  }
  .bag__seal { position: absolute; left: 0; top: 0; width: 100%; height: 40px; background: var(--bag-navy-deep); }
  .bag__tagline {
    position: absolute; top: 14px; width: 100%; text-align: center;
    font-family: "Josefin Sans", sans-serif; font-weight: 300; font-style: italic;
    font-size: 9.5px; letter-spacing: 2.4px; color: var(--tagline-blue);
  }
  .bag__zipper { position: absolute; left: 0; top: 44px; width: 100%; height: 30px; }

  .brand { position: absolute; top: 268px; width: 100%; text-align: center;
    font-family: "Josefin Sans", sans-serif; font-weight: 400; color: var(--gold); }
  .brand__name { font-size: 33px; letter-spacing: 8px; padding-left: 8px; line-height: 1; }
  .brand__sub { margin-top: 12px; font-size: 13px; letter-spacing: 5px; padding-left: 5px; }

  .label {
    position: absolute; left: 42px; top: 380px; width: 264px; height: 228px;
    background: var(--label-frame); padding: 9px;
  }
  .label__paper {
    position: relative; width: 100%; height: 100%; background: var(--label-paper);
    font-family: "Montserrat", sans-serif; color: var(--ink);
  }
  .label__origin { position: absolute; left: 10px; top: 14px; font-size: 23px; font-weight: 700; letter-spacing: 0.5px; }
  .label__badge {
    position: absolute; right: 10px; top: 10px; width: 48px; height: 40px;
    background: #3b3a38; color: var(--label-paper); text-align: center;
    font-weight: 600; font-size: 6px; line-height: 1.1; padding-top: 4px;
  }
  .label__badge strong { display: block; font-size: 12px; font-weight: 600; }
  .rule { position: absolute; left: 8px; height: 1px; background: var(--ink); }
  .field { position: absolute; left: 10px; font-size: 7.5px; font-weight: 600; letter-spacing: 0.2px; }
  .field--value { left: 86px; }
  .divider { position: absolute; width: 0; border-left: 1px dashed var(--ink); }
  .label__region-fill { position: absolute; left: 54px; top: 108px; width: 110px; height: 28px; background: var(--hatch); }
  .label__plant { position: absolute; right: 8px; top: 68px; width: 70px; height: 108px; background: linear-gradient(160deg, var(--leaf), #e7e0cc); border-radius: 4px; }
  .roast-dots { position: absolute; left: 74px; top: 158px; display: flex; gap: 6px; }
  .roast-dots span { width: 9px; height: 9px; border-radius: 50%; border: 1px solid var(--ink); }
  .roast-dots span.is-filled { background: var(--ink); }
  .label__date { position: absolute; left: 10px; top: 186px; font-size: 6px; font-weight: 600; }
  .label__date b { font-size: 13px; font-weight: 600; margin-left: 6px; vertical-align: -2px; }
  .label__weight { position: absolute; right: 8px; top: 192px; font-size: 6px; font-weight: 600; }
  .label__weight b { margin-left: 6px; font-weight: 700; }
</style>
</head>
<body>
<main class="canvas">
  <section class="bag" aria-label="Tidewell Coffee bag front">
    <div class="bag__seal"></div>
    <p class="bag__tagline">SMALL ACTS, LASTING RIPPLES IN EVERY CUP</p>
    <svg class="bag__zipper" viewBox="0 0 360 30" aria-hidden="true">
      <g stroke="#2a2940" stroke-width="1.4">
        <line x1="0" y1="6" x2="360" y2="6"/>
        <line x1="0" y1="11" x2="360" y2="11"/>
        <line x1="0" y1="16" x2="360" y2="16"/>
        <line x1="0" y1="21" x2="360" y2="21"/>
      </g>
    </svg>

    <div class="brand">
      <div class="brand__name">TIDEWELL</div>
      <div class="brand__sub">COFFEE</div>
    </div>

    <div class="label">
      <div class="label__paper">
        <h1 class="label__origin">COLOMBIA</h1>
        <div class="label__badge"><strong>100%</strong>ROASTED<br>COFFEE</div>
        <div class="rule" style="top:50px;width:176px"></div>
        <p class="field" style="top:58px">NOTES OF NUTS, AND CHOCOLATE</p>
        <div class="rule" style="top:72px;width:170px;background:var(--ink-soft)"></div>
        <p class="field" style="top:83px">PROCESSING</p>
        <div class="divider" style="left:78px;top:78px;height:24px"></div>
        <p class="field field--value" style="top:85px">SUN - DRIED</p>
        <div class="rule" style="top:103px;width:170px;background:var(--ink-soft)"></div>
        <p class="field" style="top:108px">REGION</p>
        <div class="label__region-fill" role="img" aria-label="Region name area"></div>
        <div class="label__plant" role="img" aria-label="Line illustration of a coffee branch with cherries and a bean"></div>
        <div class="rule" style="top:146px;width:170px;background:var(--ink-soft)"></div>
        <p class="field" style="top:158px">LIGHT ROAST</p>
        <div class="roast-dots" aria-label="Roast level 1 of 5">
          <span class="is-filled"></span><span></span><span></span><span></span><span></span>
        </div>
        <div class="rule" style="top:178px;width:230px"></div>
        <p class="label__date">DATE <b>JUNE 16</b></p>
        <div class="divider" style="left:104px;top:182px;height:24px"></div>
        <p class="label__weight">NET WEIGHT <b>12 OZ / 320 GR</b></p>
      </div>
    </div>
  </section>
</main>
</body>
</html>
```